Halvern Ridge Hospital

We need a template for our hospital newsletter.

I am attaching what we did for December and also what we did for January. We like the January one better, but we need to keep the old style calendar.

I am also attaching the logo.

We need the document to be easily editable so that we can change the content month to month.

Industry/Entity Type

Hospital

```html
<!DOCTYPE html>
<html lang="en">
<head>
<meta charset="utf-8">
<title>Halvern Ridge Hospital — Specialty Clinic Calendar</title>
<link rel="stylesheet" href="https://fonts.googleapis.com/css2?family=Open+Sans:wght@400;600;700;800&display=swap">
<style>
  :root{
    --navy:#1b3f7a;
    --blue:#2b6cb8;
    --bar:#1f4f9a;
    --red:#d4232b;
    --ink:#222a36;
    --grid:#9aa6b8;
    --paper:#ffffff;
    --sky-top:#6e9fd0;
    --sky-bottom:#cfe0ef;
    --stone:#c9b79a;
  }
  *{box-sizing:border-box;margin:0;padding:0}
  html,body{width:828px;height:1200px;overflow:hidden;background:var(--paper)}
  body{font-family:"Open Sans",Arial,sans-serif;color:var(--ink);position:relative}

  .masthead{position:absolute;left:0;top:0;width:828px;height:100px;display:flex;align-items:center;justify-content:space-between;padding:0 24px}
  .brand{display:flex;align-items:center;gap:10px}
  .brand-mark{width:34px;height:34px;background:var(--red)}
  .brand-name{font-weight:800;font-size:24px;color:var(--navy);line-height:1.05;width:200px}
  .contact{text-align:center;color:var(--navy);font-weight:700;font-size:16px;line-height:1.3}
  .contact strong{display:block;font-size:19px;font-weight:800}

  .hero{position:absolute;left:0;top:100px;width:828px;height:285px;background:linear-gradient(180deg,var(--sky-top) 0%,var(--sky-bottom) 55%,var(--stone) 75%,#8f8a7e 100%)}
  .hero-tagline{position:absolute;right:0;top:14px;width:430px;padding:6px 18px;background:rgba(27,63,122,.75);color:#fff;font-weight:700;font-size:17px;letter-spacing:.5px}

  .issue-bar{position:absolute;left:0;top:385px;width:828px;height:34px;background:var(--bar);color:#fff;display:flex;align-items:center;padding:0 16px;font-size:13px;font-weight:700}
  .issue-bar .issue{width:170px}
  .issue-bar .site{flex:1;text-align:center}
  .issue-bar .date{width:110px}
  .social{display:flex;gap:4px}
  .social span{width:14px;height:14px;border-radius:2px;background:#fff;opacity:.85}

  .calendar{position:absolute;left:22px;top:438px;width:784px;border-collapse:collapse;table-layout:fixed}
  .calendar caption{background:var(--red);color:#fff;font-weight:800;font-size:16px;height:30px;line-height:30px;letter-spacing:.5px}
  .calendar th{height:28px;font-size:12px;font-weight:800;color:var(--ink);border:1px solid var(--grid);text-align:center}
  .calendar td{height:134px;border:1px solid var(--grid);vertical-align:top;padding:5px 5px 4px 0;font-size:10.5px;line-height:1.25}
  .day{display:flex;height:100%}
  .num{width:22px;flex:none;text-align:center;font-size:10px;font-weight:600}
  .entries{flex:1}
  .spec{color:var(--blue);font-weight:700}
  .doc{color:var(--ink)}
</style>
</head>
<body>
  <header class="masthead">
    <div class="brand"><span class="brand-mark"></span><span class="brand-name">Halvern Ridge Hospital</span></div>
    <p class="contact">For questions or to schedule an appointment<strong>call the Specialty Clinic at (555)014-2285</strong></p>
  </header>

  <section class="hero" role="img" aria-label="Photograph of the hospital's main entrance with a covered drive-up canopy at dusk">
    <p class="hero-tagline">CARING FOR OUR COMMUNITY</p>
  </section>

  <div class="issue-bar">
    <span class="issue">ISSUE : 01</span>
    <span class="site">www.halvernridgehospital.org</span>
    <span class="date">29 JULY 2014</span>
    <span class="social"><span></span><span></span><span></span><span></span><span></span></span>
  </div>

  <table class="calendar">
    <caption>DECEMBER 2015</caption>
    <thead><tr><th>MONDAY</th><th>TUESDAY</th><th>WEDNESDAY</th><th>THURSDAY</th><th>FRIDAY</th></tr></thead>
    <tbody>
      <tr>
        <td><div class="day"><span class="num">1</span><div class="entries"></div></div></td>
        <td><div class="day"><span class="num">2</span><div class="entries"><div class="spec">Surgery/Vascular</div><div class="doc">Edwin Marlow, DO</div></div></div></td>
        <td><div class="day"><span class="num">3</span><div class="entries"><div class="spec">Surgery/Vascular</div><div class="doc">Edwin Marlow, DO</div><div class="spec">Podiatry</div><div class="doc">Randy Holcomb, DPM</div><div class="spec">Oncology / Hematology</div><div class="doc">Robert Tamsin, MD</div></div></div></td>
        <td><div class="day"><span class="num">4</span><div class="entries"><div class="spec">General Surgery</div><div class="doc">William Ashford, DO</div><div class="spec">Summit Orthotics</div><div class="doc">Ted Lindqvist</div><div class="doc">Call 555-014-1910</div></div></div></td>
        <td><div class="day"><span class="num">5</span><div class="entries"><div class="spec">Surgery/Vascular</div><div class="doc">Edwin Marlow, DO</div></div></div></td>
      </tr>
      <tr>
        <td><div class="day"><span class="num">8</span><div class="entries"><div class="spec">Pain Services</div><div class="doc">Jay Corwin CRNA</div></div></div></td>
        <td><div class="day"><span class="num">9</span><div class="entries"><div class="spec">Surgery/Vascular</div><div class="doc">Edwin Marlow, DO</div><br><div class="spec">Urology</div><div class="doc">Brian Pellow, MD</div></div></div></td>
        <td><div class="day"><span class="num">10</span><div class="entries"><div class="spec">General Surgery</div><div class="doc">William Ashford, DO</div><br><div class="spec">Oncology / Hematology</div><div class="doc">Robert Tamsin, MD</div></div></div></td>
        <td><div class="day"><span class="num">11</span><div class="entries"><div class="spec">Pulmonary Clinic</div><div class="doc">Daniel Rusk, DO</div><div class="spec">General Surgery</div><div class="doc">William Ashford, DO</div><div class="spec">Hearing Aid Specialist</div><div class="doc">Curtis Varley, H.I.S.</div></div></div></td>
        <td><div class="day"><span class="num">12</span><div class="entries"><div class="spec">Surgery/Vascular</div><div class="doc">Edwin Marlow, DO</div><br><div class="spec">Podiatry</div><div class="doc">Randy Holcomb, DPM</div></div></div></td>
      </tr>
      <tr>
        <td><div class="day"><span class="num">15</span><div class="entries"></div></div></td>
        <td><div class="day"><span class="num">16</span><div class="entries"><div class="spec">Surgery/Vascular</div><div class="doc">Edwin Marlow, DO</div><div class="spec">ENT</div><div class="doc">Stephen Oakes, MD</div><div class="spec">Dermatology</div><div class="doc">Anne Brixton , PA-C</div></div></div></td>
        <td><div class="day"><span class="num">17</span><div class="entries"><div class="spec">Surgery/Vascular</div><div class="doc">Edwin Marlow, DO</div><div class="spec">Podiatry</div><div class="doc">Randy Holcomb, DPM</div><div class="spec">Oncology / Hematology</div><div class="doc">Robert Tamsin, MD</div></div></div></td>
        <td><div class="day"><span class="num">18</span><div class="entries"><div class="spec">Ridgeline Orthopaedic</div><div class="doc">Timothy Rawle, MD</div><br><div class="spec">General Surgery</div><div class="doc">William Ashford, DO</div></div></div></td>
        <td><div class="day"><span class="num">19</span><div class="entries"><div class="spec">Surgery/Vascular</div><div class="doc">Edwin Marlow, DO</div></div></div></td>
      </tr>
      <tr>
        <td><div class="day"><span class="num">22</span><div class="entries"><div class="spec">Cardiology</div><div class="spec">Ridgeline Heart Center</div><div class="doc">Joel Starling, MD</div><div class="spec">Ridgeline Heart Device Clinic</div><div class="doc">Call 555-014-3638</div><div class="spec">Podiatry</div><div class="doc">Randy Holcomb, DPM</div></div></div></td>
        <td><div class="day"><span class="num">23</span><div class="entries"><div class="spec">Surgery/Vascular</div><div class="doc">Edwin Marlow, DO</div></div></div></td>
        <td><div class="day"><span class="num">24</span><div class="entries"><div class="spec">General Surgery</div><div class="doc">William Ashford, DO</div></div></div></td>
        <td><div class="day"><span class="num">25</span><div class="entries"></div></div></td>
        <td><div class="day"><span class="num">26</span><div class="entries"></div></div></td>
      </tr>
      <tr>
        <td><div class="day"><span class="num">29</span><div class="entries"><div class="spec">Pain Services</div><div class="doc">Jay Corwin CRNA</div></div></div></td>
        <td><div class="day"><span class="num">30</span><div class="entries"><div class="spec">Surgery/Vascular</div><div class="doc">Edwin Marlow, DO</div></div></div></td>
        <td><div class="day"><span class="num">31</span><div class="entries"><div class="spec">Podiatry</div><div class="doc">Randy Holcomb, DPM</div><div class="spec">General Surgery</div><div class="doc">William Ashford, DO</div><div class="spec">Oncology / Hematology</div><div class="doc">Robert Tamsin, MD</div></div></div></td>
        <td><div class="day"><span class="num"></span><div class="entries"></div></div></td>
        <td><div class="day"><span class="num">27</span><div class="entries"></div></div></td>
      </tr>
    </tbody>
  </table>
</body>
</html>
```